Radiant Crossing - An Exciting Mission & Book Cover Project

Help me to inspire people to live their best life! This is a mission, not just a design project.
I need a Book Cover designed to keep me inspired on the process of writing my book.
Book Title: Radiant Crossing
Tag Line: Three Clear Moves to rise past your old doubts, Brighten your Days and Walk toward Meaning!
Author: Marlis Quenby

The three steps are: Ownership, Vision and Action (Not sure if this should be on the front or back of the book cover)

The book is a self-help, motivational book. Personal development.
The cover needs to be strong and capture peoples attention, especially with competing shelf space. I almost see a fire ball of flame or explosion that will grab peoples attention.
My company is The Lantern Institute. I have added the company logo and a few pages of my presentation and topic outline to give an idea.
Maybe: The Lantern Institute logo on back of the cover. website is marlisquenby.com

THOUGHT: People should be able to take a photo of them holding the book cover showing what area of life they want Radiant Crossing in. This is why the front cover must be so visual and powerful that they want to take a photo with it. Ie. Explosion, fire, strong and bold.

Target Market(s)

Anyone who feels stuck and needs to breakthrough and move forward in life.

Industry/Entity Type

Motivation

Font styles to use
Serif
Sans Serif

Colors
ec1f27
f37122
fbed22

Requirements
Must have
• The design must be STRONG, SIMPLE, STAND OUT ON BOOK SHELVES.
Must have an open file to swap the photo and copy out.

Back Cover Page
1) Summary
2) 2-3 testimonials. One sentence.
3) About the Author (maybe with photo)
4) Lantern Institute logo
5) Website: radiantcrossing.com and marlisquenby.com
Nice to have
• If my photo works somewhere that would be great. I will change the photo later.
Added Where's Your Harbor? a nice cover example.
Should not have
• Right now I am writing the summary for the back of the cover. For now use Loreum Ipsum text and 2-3 recommendations. Again, I will get these only later.

```html
<!DOCTYPE html>
<html lang="en">
<head>
<meta charset="utf-8">
<title>Radiant Crossing — Book Cover</title>
<link rel="stylesheet" href="https://fonts.googleapis.com/css2?family=Barlow:wght@600;700&family=Archivo:wght@400&display=swap">
<style>
  :root {
    --backdrop: #c6c6c6;
    --paper: #ffffff;
    --paper-shade: #f3f3f3;
    --ink: #111111;
    --ink-soft: #2a2a2a;
    --flame-orange: #f37122;
    --flame-orange-light: #f58a45;
    --flame-red: #ec1f27;
    --flame-yellow: #fbed22;
  }
  * { box-sizing: border-box; margin: 0; padding: 0; }
  html, body {
    width: 1200px;
    height: 1200px;
    overflow: hidden;
    background: var(--backdrop);
  }
  .canvas {
    width: 1200px;
    height: 1200px;
    display: flex;
    align-items: center;
    justify-content: center;
  }
  .book-cover {
    position: relative;
    width: 740px;
    height: 1120px;
    background: linear-gradient(135deg, var(--paper) 60%, var(--paper-shade));
    display: flex;
    flex-direction: column;
    align-items: center;
    text-align: center;
  }
  .tagline {
    margin-top: 58px;
    font-family: "Archivo", sans-serif;
    font-size: 19px;
    line-height: 1.5;
    letter-spacing: 0.09em;
    color: var(--ink-soft);
  }
  .title {
    margin-top: 118px;
    font-family: "Barlow", sans-serif;
    font-weight: 600;
    line-height: 0.92;
    letter-spacing: 0.02em;
  }
  .title-accent {
    display: block;
    font-size: 150px;
    color: var(--flame-orange);
    background: linear-gradient(90deg, var(--flame-orange-light), var(--flame-orange));
    -webkit-background-clip: text;
    background-clip: text;
    -webkit-text-fill-color: transparent;
  }
  .title-main {
    display: block;
    font-size: 132px;
    color: var(--ink);
  }
  .fireball {
    margin-top: 78px;
    width: 340px;
    height: 340px;
    border-radius: 50%;
    background: radial-gradient(circle at 42% 45%,
      var(--flame-yellow) 0%,
      #fbc02d 30%,
      var(--flame-orange) 60%,
      var(--flame-red) 82%,
      rgba(236, 31, 39, 0) 100%);
    box-shadow: 0 0 50px 14px rgba(243, 113, 34, 0.22);
  }
  .author {
    margin-top: auto;
    margin-bottom: 96px;
    font-family: "Barlow", sans-serif;
    font-weight: 700;
    font-size: 84px;
    letter-spacing: 0.02em;
    color: var(--ink);
  }
</style>
</head>
<body>
  <main class="canvas">
    <section class="book-cover">
      <p class="tagline">Three Clear Moves to rise past your old doubts,<br>Brighten your Days and Walk toward Meaning!</p>
      <h1 class="title">
        <span class="title-accent">RADIANT</span>
        <span class="title-main">CROSSING</span>
      </h1>
      <div class="fireball" role="img" aria-label="Photograph of a blazing ball of fire"></div>
      <p class="author">MARLIS QUENBY</p>
    </section>
  </main>
</body>
</html>
```